TLW Indianapolis Website

Create a web design to represent our image as an up and coming, technology focused neuropsychological practice.
TLW is short for Bright Harbor Pediatric Collective, we specialize in neuropsychological assessments and intervention in pediatric populations. Directed at a more affluent population, our target market is parents age 25-30+ with children ages 2-22.
We would like a coming soon web page that would allow for email submission to be notified when we are online, as well as provide our contact information for immediate referrals.
Target Market(s)
Parents aged 25+ with children aged 2-22
Industry/Entity Type
Group
Requirements
Must have
- Must provide our contact information as follows:
Skype number: 4089231576 (would be nice to have a Skype direct call button)
Email Address: contact@tlwclinicdemo.com
Our brief summary of what we do:
"At Bright Harbor Pediatric Collective we are committed to providing you with an unsurpassable quality of care. Under the direction of Dr. Rosalind T. Abernathy, one of nine Board Certified Clinical Neuropsychologists in the state of Indiana, TLW has developed a unique approach of utilizing technology to aide in neurobehavioral assessments like nobody else in the business. Our revolutionary utilization of technology as a diagnostic tool, coupled with our traditionally rooted experience and expertise, create the ideal package to insure your child’s future success, both in and out of the classroom."
Nice to have
- Nice to have the ability for patients to fill out a form with basic demographics (name, age, city, email, phone) along with a brief note on services they're seeking on a separate page.
A separate page that contains our consent forms that would be available for download (see attached).

```html
<!DOCTYPE html>
<html lang="en">
<head>
<meta charset="utf-8">
<title>Bright Harbor Pediatric Collective</title>
<link rel="stylesheet" href="https://fonts.googleapis.com/css2?family=Questrial&display=swap">
<style>
  :root {
    --bg-light: #f3f4f5;
    --bg-mid: #dfe4e8;
    --scrub-blue: #9fb4cf;
    --coat-white: #fbfbfb;
    --ink: #2f3133;
    --title-ink: #1d1d1f;
    --nav-ink: #9a9c9e;
    --accent-blue: #39a8e0;
    --enter-ink: #5f7f9e;
    --panel: rgba(255, 255, 255, 0.55);
    --field-line: #c3ccd4;
    --footer-ink: #8e9092;
    --brand-dot: #6aa8d8;
  }
  * { margin: 0; padding: 0; box-sizing: border-box; }
  html, body { width: 1200px; height: 800px; overflow: hidden; }
  body {
    font-family: "Questrial", "Century Gothic", sans-serif;
    color: var(--ink);
    background: var(--bg-light);
  }
  .page { position: relative; width: 1200px; height: 800px; overflow: hidden; }

  .hero-photo {
    position: absolute; inset: 0;
    background:
      radial-gradient(ellipse 230px 420px at 880px 560px, var(--coat-white) 0%, rgba(251,251,251,0) 100%),
      radial-gradient(ellipse 120px 300px at 660px 560px, rgba(159,180,207,0.55) 0%, rgba(159,180,207,0) 100%),
      radial-gradient(ellipse 110px 300px at 440px 560px, rgba(159,180,207,0.5) 0%, rgba(159,180,207,0) 100%),
      linear-gradient(90deg, var(--bg-mid) 0%, var(--bg-light) 55%, #ecedee 100%);
  }

  .brand {
    position: absolute; left: 28px; top: 34px;
    display: flex; align-items: center; gap: 26px;
  }
  .brand-dot {
    width: 96px; height: 96px; border-radius: 50%;
    background: var(--brand-dot); opacity: 0.85;
  }
  .brand-name {
    font-size: 28px; letter-spacing: 1.5px;
    color: var(--title-ink); text-transform: uppercase;
    margin-top: 6px;
  }

  .main-nav {
    position: absolute; left: 47px; top: 140px;
    display: flex; gap: 11px;
    font-size: 20px; color: var(--nav-ink); letter-spacing: 0.5px;
  }

  .welcome-panel {
    position: absolute; left: 45px; top: 200px;
    width: 574px; height: 521px;
    background: var(--panel); border-radius: 10px;
  }
  .welcome-title {
    position: absolute; left: 30px; top: 30px;
    font-size: 28px; font-weight: 400; letter-spacing: 1px;
    color: var(--accent-blue);
  }
  .welcome-text {
    position: absolute; left: 30px; top: 82px;
    width: 514px;
    font-size: 17.5px; line-height: 30px; letter-spacing: 0.9px;
    text-align: justify; hyphens: auto; color: var(--ink);
  }
  .contact-line {
    position: absolute; left: 30px; top: 424px;
    font-size: 15px; letter-spacing: 0.6px; color: var(--ink);
  }
  .contact-line .label { color: var(--accent-blue); }
  .notify-form {
    position: absolute; left: 30px; top: 460px;
    display: flex; gap: 8px;
  }
  .notify-input {
    width: 250px; height: 36px; padding: 0 12px;
    font: inherit; font-size: 14px; letter-spacing: 0.5px;
    color: var(--ink); background: rgba(255,255,255,0.85);
    border: 1px solid var(--field-line); border-radius: 4px;
  }
  .notify-button {
    height: 36px; padding: 0 16px;
    font: inherit; font-size: 14px; letter-spacing: 1px;
    color: #fff; background: var(--accent-blue);
    border: none; border-radius: 4px;
  }
  .enter-link {
    position: absolute; right: 22px; bottom: 20px;
    font-size: 24px; letter-spacing: 1px; color: var(--enter-ink);
    text-decoration: none; line-height: 36px;
  }

  .site-footer {
    position: absolute; left: 53px; top: 762px;
    font-size: 11.5px; letter-spacing: 0.6px;
    color: var(--footer-ink); text-transform: uppercase;
  }
</style>
</head>
<body>
<div class="page">
  <div class="hero-photo" role="img" aria-label="Smiling young doctor in a white coat with a stethoscope, with blurred medical staff in scrubs behind her in a bright clinic"></div>

  <header class="brand">
    <span class="brand-dot"></span>
    <span class="brand-name">Bright Harbor Pediatric Collective</span>
  </header>

  <nav class="main-nav">
    <span>Main</span>
    <span>About</span>
    <span>TLWindianapolis</span>
    <span>Our Technology</span>
    <span>Contact Us</span>
  </nav>

  <section class="welcome-panel">
    <h1 class="welcome-title">WELCOME!</h1>
    <p class="welcome-text" lang="en">At Bright Harbor Pediatric Collective we are committed to providing you with an unsurpassable quality of care. Under the direction of Dr. Rosalind T. Abernathy, one of nine Board Certified Clinical Neuropsychologists in the state of Indiana, TLW has developed a unique approach of utilizing technology to aide in neurobehavioral assessments like nobody else in the business. Our revolutionary utilization of technology as a diagnostic tool, coupled with our traditionally rooted experience and expertise, create the ideal package to insure your child’s future success, both in and out of the classroom.</p>
    <p class="contact-line"><span class="label">Skype</span> 4089231576 &nbsp;·&nbsp; <span class="label">Email</span> contact@tlwclinicdemo.com</p>
    <form class="notify-form" action="#">
      <input class="notify-input" type="email" placeholder="Your email address">
      <button class="notify-button" type="submit">NOTIFY ME</button>
    </form>
    <a class="enter-link" href="#">+ENTER</a>
  </section>

  <footer class="site-footer">© Bright Harbor Pediatric Collective</footer>
</div>
</body>
</html>
```